Red Gum Business Card Design

We are a new small business specialising in under ground cable jointing and excavation works in NSW Australia.
Design I'm looking for is incorporating the Australian flag & excavator with out being to cheesy.
Maybe a faded washed out flag to help with overload of colour? & so its not the main focus.
Very open to creative out of the box designs!

Target Market(s)

Building & Construction

Industry/Entity Type

Construction

Contact Information for Business Card

Red Gum Cable Jointing & Excavations
Owen Falkirk

Ph: 0438 605 312
E: owen.falkirk@tallmail.example

Reverse Side
Services we offer:
High Voltage & Low Voltage Cable Jointing
Polymeric & paperlead jointing & terminations
Trenching & Auger Drilling 150 - 600mm
Site preparation / leveling / clearing
Driveway / Footpath / Turf Prep
Rubbish Removal
Tree & Stump removal
Footings & Post holes
Drainage
Service Installs
Gravels & Sands available
Any general Earth moving needs
Reliable Free Quotes
Fully Insured

Font styles to use
Serif
Script

Requirements
Nice to have
• small excavator (See uploaded picture)

```html
<!DOCTYPE html>
<html lang="en">
<head>
<meta charset="utf-8">
<title>Red Gum Business Card Design</title>
<link rel="stylesheet" href="https://fonts.googleapis.com/css2?family=Lobster&family=Tinos&display=swap">
<style>
  :root {
    --ink: #2b1a23;
    --paper: #ffffff;
    --stage: #e9e6e2;
    --sky-top: #7d7a80;
    --sky-mid: #c4c3c7;
    --sky-low: #eeeeef;
    --cream: #f4f1ef;
  }
  * { margin: 0; padding: 0; box-sizing: border-box; }
  html, body { width: 1200px; height: 933px; overflow: hidden; }
  body { background: var(--stage); position: relative; font-family: "Tinos", "Times New Roman", serif; }

  .card { position: absolute; overflow: hidden; box-shadow: 0 4px 14px rgba(0,0,0,.25); }

  /* Front */
  .card-front { left: 274px; top: 64px; width: 652px; height: 374px; background: var(--paper); color: var(--ink); }
  .company-name {
    position: absolute; left: 0; right: 0; top: 52px; text-align: center;
    font-family: "Lobster", cursive; font-size: 37px; font-weight: 400; letter-spacing: .2px;
  }
  .contact { position: absolute; right: 35px; top: 168px; text-align: right; }
  .person-name { font-size: 32px; line-height: 1; margin-bottom: 28px; }
  .contact-line { display: flex; justify-content: flex-end; align-items: center; gap: 22px; font-size: 21px; line-height: 28px; }
  .contact-line svg { width: 15px; height: 15px; flex: none; }
  .mascot-area {
    position: absolute; left: 134px; top: 198px; width: 150px; height: 116px;
    background: radial-gradient(ellipse at 50% 55%, rgba(43,26,35,.16) 0%, rgba(43,26,35,.06) 60%, rgba(43,26,35,0) 100%);
  }
  .ground { position: absolute; left: 0; top: 0; width: 652px; height: 374px; }

  /* Back */
  .card-back { left: 259px; top: 494px; width: 668px; height: 382px; background: var(--ink); color: var(--cream); }
  .machine-photo {
    position: absolute; right: 0; top: 0; width: 400px; height: 100%;
    background:
      linear-gradient(90deg,
        rgba(43,26,35,1) 0%,
        rgba(43,26,35,.92) 14%,
        rgba(43,26,35,.75) 28%,
        rgba(43,26,35,.5) 42%,
        rgba(43,26,35,.26) 56%,
        rgba(43,26,35,.1) 70%,
        rgba(43,26,35,0) 85%),
      linear-gradient(180deg, var(--sky-top) 0%, var(--sky-mid) 40%, var(--sky-low) 100%);
  }
  .services-title {
    position: absolute; left: 372px; top: 58px; white-space: nowrap;
    font-family: "Lobster", cursive; font-size: 43px; font-weight: 400; color: #fff;
    text-shadow: 1px 2px 3px rgba(0,0,0,.55);
  }
  .service-list { position: absolute; left: 18px; top: 10px; list-style: none; }
  .service-list li { display: flex; align-items: center; font-size: 17.5px; line-height: 25.8px; }
  .service-list li::before {
    content: ""; width: 7px; height: 7px; border: 2px solid var(--cream); border-radius: 50%;
    margin-right: 14px; flex: none;
  }
</style>
</head>
<body>

<section class="card card-front">
  <h1 class="company-name">Red Gum Cable Jointing &amp; Excavations</h1>
  <div class="mascot-area" role="img" aria-label="Silhouette of a hopping kangaroo"></div>
  <svg class="ground" viewBox="0 0 652 374" aria-hidden="true">
    <polygon points="0,314 214,314 278,340 0,340" fill="var(--ink)"/>
    <rect x="0" y="346" width="652" height="28" fill="var(--ink)"/>
  </svg>
  <div class="contact">
    <p class="person-name">Owen Falkirk</p>
    <p class="contact-line">0438 605 312
      <svg viewBox="0 0 16 16" aria-label="Phone"><rect x="0.5" y="0.5" width="15" height="15" fill="var(--ink)"/><path d="M3 6 Q8 2 13 6 L12 8 L10 7 L10 6 Q8 5 6 6 L6 7 L4 8 Z M5 9 H11 V13 H5 Z" fill="#fff"/></svg>
    </p>
    <p class="contact-line">owen.falkirk@tallmail.example
      <svg viewBox="0 0 16 16" aria-label="Email"><rect x="0.5" y="0.5" width="15" height="15" fill="var(--ink)"/><rect x="3" y="4.5" width="10" height="7" fill="#fff"/><path d="M3 4.5 L8 8.5 L13 4.5" stroke="var(--ink)" fill="none"/></svg>
    </p>
  </div>
</section>

<section class="card card-back">
  <div class="machine-photo" role="img" aria-label="Photo of an orange mini excavator against a cloudy grey sky"></div>
  <h2 class="services-title">Services we offer:</h2>
  <ul class="service-list">
    <li>High Voltage &amp; Low Voltage Cable Jointing</li>
    <li>Polymeric &amp; paperlead jointing &amp; terminations</li>
    <li>Trenching &amp; Auger Drilling 150 - 600mm</li>
    <li>Site preparation / leveling / clearing</li>
    <li>Driveway / Footpath / Turf Prep</li>
    <li>Rubbish Removal</li>
    <li>Tree &amp; Stump removal</li>
    <li>Footings &amp; Post holes</li>
    <li>Drainage</li>
    <li>Service Installs</li>
    <li>Gravels &amp; Sands available</li>
    <li>Any general Earth moving needs</li>
    <li>Reliable Free Quotes</li>
    <li>Fully Insured</li>
  </ul>
</section>

</body>
</html>
```